Brisk Harbour Co - labels

I have my logo now so its time to proceed with the labels.
The product is organic juices and smoothies. They will be served in Mason jar's and sold as a premium hand made product into the CBD and outlets around Perth such as yoga studios gyms, cafe's etc. Cleanses to individuals etc.
I have attached the logo and a mock of what I would like to see.
I think the logo and the raw organic, handmade look will work with the Chalkboard design and maybe some bunting to brighten the design.
There is currently approx. 10 Juices and Smoothies to the range so I will need to settle on the design and then have you create a label for each one, once settled on the design.
If you have any questions please let me know.

Text on label:
Raw, Organic, Hand Made, Gluten-Free, Dairy-Free

Juice
Chasing Bright Dawn
Kale, Apple, Celery, Dandelion, Lemon & Ginger

This product is FRESH. Shake before you enjoy!!!

Label size. highest point for height 70 - 75mm. Length 200mm
I also have more wording and nutritional guide for Australian Standards. I will update soon.
Thank you

    Happy Friday Designers!!!

Well I have just increased the budget to $300. I hope this helps to get some designs coming through. If you need anything else from me please send a message.

I look forward to receiving your designs soon and thank you for working with me on my business. this is such an exciting time for me and you guys are making my dream a reality so thank you for your time.

Regards,

Bronwyn

Reason: I have not received many designs so extending for a few more days.

Industry/Entity Type

Cafe

Requirements
Must have
• Wording - Hand Made
Raw, Organic, Gluten-Free, Dairy-Free
Nice to have
• A chalk board with Juice or Smoothie - Name and ingredients
Bunting I think will work well with the design of logo and chalk board plus bring some colour.

```html
<!DOCTYPE html>
<html lang="en">
<head>
<meta charset="utf-8">
<title>Brisk Harbour Co – Juice Label</title>
<link rel="stylesheet" href="https://fonts.googleapis.com/css2?family=Cinzel:wght@700&family=Cabin+Sketch:wght@400;700&family=Gochi+Hand&display=swap">
<style>
  :root {
    --page: #ffffff;
    --gold: #b08a3e;
    --gold-light: #e0c27a;
    --sky-top: #4f8fd6;
    --sky-mid: #a9d0f0;
    --grass: #4f9a2a;
    --grass-dark: #2f6a18;
    --panel: #1f5a2a;
    --lime: #d6e026;
    --lime-text: #d9e021;
    --chalk: #f2f2ee;
    --board: #34423a;
    --board-dark: #27322c;
    --wood: #7a3a1c;
    --wood-dark: #4e220f;
    --white: #ffffff;
  }
  html, body {
    margin: 0;
    padding: 0;
    width: 811px;
    height: 1200px;
    overflow: hidden;
    background: var(--page);
  }
  .label {
    display: block;
    width: 811px;
    height: 1200px;
  }
  .claim {
    font-family: "Cinzel", serif;
    font-weight: 700;
    fill: var(--white);
    font-size: 40px;
  }
  .flavour-title {
    font-family: "Cinzel", serif;
    font-weight: 700;
    fill: var(--lime-text);
    font-size: 54px;
  }
  .brand-name {
    font-family: "Cinzel", serif;
    font-weight: 700;
    fill: var(--panel);
    font-size: 40px;
  }
  .chalk-line {
    font-family: "Cabin Sketch", cursive;
    font-weight: 400;
    fill: var(--chalk);
    font-size: 82px;
  }
  .chalk-product {
    font-family: "Cabin Sketch", cursive;
    font-weight: 700;
    fill: var(--chalk);
    font-size: 104px;
  }
  .chalk-note {
    font-family: "Gochi Hand", cursive;
    fill: var(--lime-text);
    font-size: 46px;
  }
  .chalk-note--small {
    font-size: 30px;
  }
  .freshness {
    font-family: "Cinzel", serif;
    font-weight: 700;
    fill: var(--lime-text);
    font-size: 30px;
  }
</style>
</head>
<body>
<svg class="label" viewBox="0 0 811 1200" xmlns="http://www.w3.org/2000/svg">
  <defs>
    <clipPath id="label-shape">
      <path d="M10,170 Q70,165 70,75 Q405,-20 741,75 Q741,165 801,170 L801,1030 Q741,1040 741,1130 Q405,1225 70,1130 Q70,1040 10,1030 Z"/>
    </clipPath>
    <linearGradient id="scene-fill" x1="0" y1="0" x2="0" y2="1">
      <stop offset="0" stop-color="var(--sky-top)"/>
      <stop offset="0.55" stop-color="var(--sky-mid)"/>
      <stop offset="0.68" stop-color="var(--sky-mid)"/>
      <stop offset="0.72" stop-color="var(--grass)"/>
      <stop offset="1" stop-color="var(--grass-dark)"/>
    </linearGradient>
    <radialGradient id="board-fill" cx="0.5" cy="0.45" r="0.7">
      <stop offset="0" stop-color="var(--board)"/>
      <stop offset="1" stop-color="var(--board-dark)"/>
    </radialGradient>
    <path id="arc-left" d="M95,300 A300,300 0 0 0 345,478"/>
    <path id="arc-right" d="M490,478 A300,300 0 0 0 725,300"/>
  </defs>

  <!-- sky and meadow backdrop -->
  <g clip-path="url(#label-shape)">
    <rect class="backdrop" role="img" aria-label="Sunny blue sky with clouds over a green meadow and lake" x="0" y="0" width="811" height="1200" fill="url(#scene-fill)"/>
  </g>
  <path class="label-border" d="M10,170 Q70,165 70,75 Q405,-20 741,75 Q741,165 801,170 L801,1030 Q741,1040 741,1130 Q405,1225 70,1130 Q70,1040 10,1030 Z" fill="none" stroke="var(--gold)" stroke-width="8"/>

  <!-- green panel -->
  <path class="panel" d="M50,280 L215,280 A200,200 0 0 0 610,280 L760,280 L760,1120 Q600,1165 405,1165 Q210,1165 50,1120 Z" fill="var(--panel)" stroke="var(--gold-light)" stroke-width="3"/>

  <!-- brand mark -->
  <circle class="brand-disc" cx="412" cy="225" r="180" fill="var(--lime)"/>
  <text class="brand-name" x="412" y="215" text-anchor="middle">Brisk Harbour</text>
  <text class="brand-name" x="412" y="263" text-anchor="middle">Co</text>

  <!-- claims -->
  <text class="claim"><textPath href="#arc-left" startOffset="50%" text-anchor="middle">Gluten Free</textPath></text>
  <text class="claim" x="418" y="485" text-anchor="middle">Raw</text>
  <text class="claim"><textPath href="#arc-right" startOffset="50%" text-anchor="middle">Dairy Free</textPath></text>

  <text class="flavour-title" x="405" y="552" text-anchor="middle" textLength="660" lengthAdjust="spacingAndGlyphs">Chasing Bright Dawn</text>

  <!-- chalkboard -->
  <rect class="board-frame" x="74" y="564" width="662" height="472" fill="var(--wood)" stroke="var(--wood-dark)" stroke-width="4"/>
  <rect class="board" x="98" y="588" width="614" height="424" fill="url(#board-fill)"/>

  <text class="chalk-line" x="150" y="680" textLength="350" lengthAdjust="spacingAndGlyphs">CELERY</text>
  <text class="chalk-note" x="512" y="628" transform="rotate(18 512 628)">Organic</text>
  <text class="chalk-line" x="205" y="778" textLength="455" lengthAdjust="spacingAndGlyphs">CUCUMBER</text>
  <text class="chalk-line" x="130" y="868" textLength="560" lengthAdjust="spacingAndGlyphs">LEMON GINGER</text>
  <text class="chalk-product" x="232" y="988" textLength="330" lengthAdjust="spacingAndGlyphs">Juice</text>
  <rect class="chalk-stick" role="img" aria-label="Piece of chalk" x="590" y="935" width="38" height="18" rx="3" fill="var(--chalk)" transform="rotate(-12 609 944)"/>
  <text class="chalk-note chalk-note--small" x="578" y="1000" transform="rotate(-6 578 1000)">Hand Made</text>

  <!-- freshness note -->
  <text class="freshness" x="405" y="1082" text-anchor="middle">This product is fresh</text>
  <text class="freshness" x="405" y="1113" text-anchor="middle">Shake before you enjoy</text>
</svg>
</body>
</html>
```